K.R.O.U.B.S. Content Framework Infographic

I am looking to take my basic infographic to the next level. I need to to translate the content marketing concept that is outlined in the uploaded file. I have attached the content and the image I would like used. I am not stuck on the colors represented in the image but do want to see a variety of options.

Target Market(s)

Companies that are looking for a content marketing strategy, SEO Agencies, marketing agencies

Industry/Entity Type

Digital marketing, SEO

Font styles to use
Other font styles liked:
• arial, calibri are fine

Colors
0054AA
0677BA
7BADD7
CADEEF
E8F1F8
0094D4
00A9DD
6FCCEA
C7EBF8
E9F6FB
00AB8E
00BBA5
67D7C9
C6EFE9
E9F9F6
59FF00
82FF00
B8FF75
E3FFCB
F4FFEA
EE7325
F08F49
F5BC92
FAE3D3
FDF4ED
EB3D1F
EC4F4E
F09395
F8D3D4
FCEDEE

Requirements
Must have
• The image that I provided with the content breakdown with section connectors to the image
Nice to have
• a few different way to present the data

```html
<!DOCTYPE html>
<html lang="en">
<head>
<meta charset="utf-8">
<title>K.R.O.U.B.S. Content Framework</title>
<link href="https://fonts.googleapis.com/css2?family=Lato:wght@400;700&display=swap" rel="stylesheet">
<style>
  :root {
    --page: #ffffff;
    --panel: #f5f5f5;
    --ink: #111111;
    --accent: #EC4F4E;
    --multimedia: #F8D3D4;
    --multimedia-line: #F09395;
    --engagement: #B8FF75;
    --engagement-line: #59FF00;
    --expertise: #F5BC92;
    --expertise-line: #EE7325;
    --experience: #F09395;
    --experience-line: #EB3D1F;
    --authority: #7BADD7;
    --authority-line: #0054AA;
    --trust: #67D7C9;
    --trust-line: #00AB8E;
    --rule: #111111;
  }
  * { margin: 0; padding: 0; box-sizing: border-box; }
  html, body {
    width: 911px; height: 1200px; overflow: hidden;
    background: var(--page);
    font-family: "Lato", Arial, sans-serif;
    color: var(--ink);
  }
  .panel {
    position: absolute; left: 45px; top: 50px;
    width: 816px; height: 1107px;
    background: var(--panel);
  }
  .headline {
    position: absolute; left: 0; right: 0; top: 104px;
    text-align: center; font-size: 16.3px; font-weight: 700;
    letter-spacing: -0.2px;
  }
  .headline .framework { color: var(--accent); font-weight: 400; }
  .intro {
    position: absolute; left: 136px; top: 150px; width: 640px;
    font-size: 10.5px; line-height: 18px; letter-spacing: -0.05px;
  }
  .hero-figure {
    position: absolute; left: 255px; top: 318px;
    width: 437px; height: 226px;
    border-radius: 46% 40% 30% 38% / 50% 45% 40% 50%;
    background: linear-gradient(100deg,
      var(--expertise) 0%, var(--authority) 28%, var(--trust) 44%,
      var(--multimedia) 58%, var(--experience) 74%, var(--engagement) 100%);
  }
  .connectors {
    position: absolute; left: 0; top: 0;
    width: 911px; height: 1200px;
    pointer-events: none;
  }
  .connector { fill: none; stroke-width: 2; }
  .pillars {
    position: absolute; left: 136px; top: 574px;
    width: 650px; height: 500px;
    display: grid;
    grid-template-columns: 1fr 1fr;
    grid-template-rows: 168px 144px 188px;
    border: 1.5px solid var(--rule);
  }
  .pillar {
    padding: 24px 22px 0 29px;
    font-size: 10.6px; line-height: 16.3px;
    border-right: 1px solid var(--rule);
    border-bottom: 1px solid var(--rule);
  }
  .pillar:nth-child(2n) { border-right: none; }
  .pillar:nth-last-child(-n+2) { border-bottom: none; }
  .pillar strong { font-weight: 700; }
  .pillar--multimedia { background: var(--multimedia); }
  .pillar--engagement { background: var(--engagement); }
  .pillar--expertise { background: var(--expertise); }
  .pillar--experience { background: var(--experience); }
  .pillar--authority { background: var(--authority); }
  .pillar--trust { background: var(--trust); }
</style>
</head>
<body>
  <div class="panel"></div>

  <h1 class="headline">Putting <span class="framework">K.R.O.U.B.S.</span> on the bone for the User &amp; Findora To Chew on</h1>

  <p class="intro">In SEO content is still king.&nbsp; What has changed with content is not the content but the delivery of that content.&nbsp; People these days are consuming content in so many different places &amp; formats that it makes it difficult to create engaging content that ranks and converts.&nbsp; Some people prefer to continue reading webpages to find the information they are looking for.&nbsp; Some prefer to see the pictures because they are more visual than contextual.&nbsp; Others would prefer to just watch video on Vidstream or other online video platforms, and in some cases it is more of an auditory way such as podcast &amp; streaming radio platforms.&nbsp; This infographic will breakdown how all of the pieces fit together to get “K.R.O.U.B.S.” on the bone of content.</p>

  <div class="hero-figure" role="img" aria-label="Illustration of a pig divided into butcher-style cuts labelled Expertise, Trust, Multimedia, Authority, Experience and Engagement"></div>

  <svg class="connectors" viewBox="0 0 911 1200" aria-hidden="true">
    <path class="connector" stroke="var(--authority-line)" d="M300 536 V552 H92 V980 H136"/>
    <path class="connector" stroke="var(--expertise-line)" d="M340 538 V558 H107 V814 H136"/>
    <path class="connector" stroke="var(--multimedia-line)" d="M380 540 V564 H122 V658 H136"/>
    <path class="connector" stroke="var(--engagement-line)" d="M560 540 V564 H800 V658 H786"/>
    <path class="connector" stroke="var(--experience-line)" d="M600 538 V558 H815 V814 H786"/>
    <path class="connector" stroke="var(--trust-line)" d="M640 534 V552 H830 V980 H786"/>
    <circle cx="300" cy="536" r="4" fill="var(--authority-line)"/>
    <circle cx="340" cy="538" r="4" fill="var(--expertise-line)"/>
    <circle cx="380" cy="540" r="4" fill="var(--multimedia-line)"/>
    <circle cx="560" cy="540" r="4" fill="var(--engagement-line)"/>
    <circle cx="600" cy="538" r="4" fill="var(--experience-line)"/>
    <circle cx="640" cy="534" r="4" fill="var(--trust-line)"/>
  </svg>

  <section class="pillars">
    <div class="pillar pillar--multimedia"><strong>MULTIMEDIA:</strong> “Multimedia”consists of infographics, specific images, embedded videos, and other types content aside from the written word.&nbsp; By doing this you provide the same content to audiences that differ based on how they choose to consume content. Online content marketing with multimedia is highly engaging as it presents desired information in a multifaceted but direct and timely manner.</div>
    <div class="pillar pillar--engagement"><strong>ENGAGEMENT:</strong> “Engagement” is essential for views and conversion as it keeps readers locked in on content to the point that they are more likely to move through the website experience and at least consider the value offered in the minutes, hours, days, and weeks that follow their website visit.</div>
    <div class="pillar pillar--expertise"><strong>EXPERTISE:</strong> “Expertise” refers to the content writer's level of knowledge or skill in a specific subject area that is relevant to the user's search query. High-quality content should be created by someone with relevant expertise in the topic being discussed</div>
    <div class="pillar pillar--experience"><strong>EXPERIENCE:</strong> “Experience” in short means that Findora values firsthand or life experience of the author on the topic a page is about. It is important because often searchers want to know first-hand information before they decide to purchase something or use a certain service.</div>
    <div class="pillar pillar--authority"><strong>AUTHORITATIVENESS:</strong> “Authoritativeness” refers to the credibility of the content and the website it is hosted on. Authoritativeness can be established through the quality of the content, the site's reputation, author’s reputation, external links &amp; content citations, and the credentials of the content creator.</div>
    <div class="pillar pillar--trust"><strong>TRUSTWORTHINESS:</strong> “Trustworthiness” is the final result of doing all of the above.&nbsp; If you can write content that is helpful, knowledge, first hand based on experience from someone who is an expert in their field, you get the trust of users consuming your content.&nbsp; If you can gain the user’s trust about your content,&nbsp; Findora and other search engines will “Trust” you and will provide you with the organic visibility we all strive for..</div>
  </section>
</body>
</html>
```